Business Card Design Project

Doctor, Pain Management. Need a new business card design with appointment info on the back. New address is 18 Whitcombe Road, Suite 305, Linden Falls, NJ 07799. Right now I believe the rest of the information is staying the same.

```html
<!DOCTYPE html>
<html lang="en">
<head>
<meta charset="utf-8">
<title>Gentle Relief Pain Care – Business Card</title>
<link href="https://fonts.googleapis.com/css2?family=Open+Sans:ital,wght@0,400;0,600;0,700;1,400&family=Roboto+Condensed:wght@400;700&display=swap" rel="stylesheet">
<style>
  :root {
    --backdrop: #e9e6e1;
    --card-dark: #1c1d1f;
    --card-dark-hi: #2c2d30;
    --card-light: #ffffff;
    --accent-blue: #5cc6ec;
    --accent-yellow: #e8e23a;
    --text-light: #e6e6e6;
    --text-dark: #1a1a1a;
    --rule: #6d6e70;
    --dotted: #8a8a8a;
  }
  * { box-sizing: border-box; margin: 0; padding: 0; }
  html, body { width: 1200px; height: 950px; overflow: hidden; }
  body {
    background: var(--backdrop);
    font-family: "Open Sans", sans-serif;
    position: relative;
  }
  .card {
    position: absolute;
    width: 600px;
    height: 343px;
    border-radius: 3px;
    box-shadow: 0 10px 24px rgba(0,0,0,.22);
    overflow: hidden;
  }

  /* Front */
  .card--front {
    left: 60px; top: 110px;
    background: linear-gradient(135deg, var(--card-dark-hi) 0%, var(--card-dark) 55%, #141517 100%);
    color: var(--text-light);
  }
  .brand {
    position: absolute; left: 190px; top: 40px;
    display: flex; align-items: center; gap: 12px;
  }
  .brand__dot {
    width: 30px; height: 30px; border-radius: 50%;
    background: var(--accent-blue);
  }
  .brand__name {
    font-size: 24px; font-weight: 400; color: var(--accent-yellow);
    letter-spacing: .5px;
  }
  .address {
    position: absolute; right: 40px; top: 94px;
    text-align: right; font-size: 14px; line-height: 1.4; font-style: normal;
  }
  .divider {
    position: absolute; left: 40px; right: 40px; top: 162px;
    height: 1px; background: var(--rule);
  }
  .person { position: absolute; left: 40px; top: 170px; }
  .person__name {
    font-family: "Roboto Condensed", sans-serif;
    font-size: 24px; font-weight: 400; color: var(--accent-blue);
    letter-spacing: .3px; line-height: 1.25;
  }
  .person__title {
    font-family: "Roboto Condensed", sans-serif;
    font-size: 16px; font-weight: 700; color: var(--accent-yellow);
    line-height: 1.25;
  }
  .person__rule { width: 250px; height: 1px; background: var(--rule); margin: 7px 0 6px; }
  .contacts { list-style: none; font-size: 14px; line-height: 1.4; }
  .contacts li { display: flex; align-items: center; gap: 9px; }
  .contacts svg { width: 12px; height: 12px; flex: none; }
  .edge {
    position: absolute; left: 0; right: 0; bottom: 0; height: 12px;
    background: var(--accent-blue);
    border-top: 2px solid var(--accent-yellow);
  }

  /* Back */
  .card--back {
    left: 540px; top: 497px;
    background: var(--card-light);
    color: var(--text-dark);
    padding: 32px 36px;
  }
  .appt__title { font-size: 24px; font-weight: 700; margin-bottom: 30px; }
  .field { display: flex; align-items: flex-end; gap: 8px; font-size: 16px; margin-bottom: 30px; }
  .field__line { flex: 1; border-bottom: 2px dotted var(--dotted); height: 18px; }
  .field__suffix { font-size: 12px; color: #555; }
  .days { display: flex; justify-content: space-between; font-size: 15px; margin: 4px 0 30px; }
  .day { display: flex; align-items: center; gap: 5px; }
  .day__box { width: 15px; height: 15px; border: 1.5px solid var(--text-dark); }
  .note { font-size: 12.5px; font-style: italic; line-height: 1.45; }
</style>
</head>
<body>

<section class="card card--front" aria-label="Business card front">
  <div class="brand">
    <span class="brand__dot"></span>
    <span class="brand__name">Gentle Relief Pain Care</span>
  </div>

  <address class="address">
    18 Whitcombe Road<br>Suite 305<br>Linden Falls, NJ 07799
  </address>

  <div class="divider"></div>

  <div class="person">
    <div class="person__name">MEILIN ZHAO, M.D., PH.D.</div>
    <div class="person__title">Board Certified Anesthesiologist</div>
    <div class="person__rule"></div>
    <ul class="contacts">
      <li><svg viewBox="0 0 12 12"><path d="M3 1l2 2.5-1.2 1.3a7 7 0 0 0 3.4 3.4L8.5 7 11 9l-1 2C5 11 1 7 1 2z" fill="#e6e6e6"/></svg>973.555.0142</li>
      <li><svg viewBox="0 0 12 12"><rect x="1" y="4" width="10" height="6" fill="#e6e6e6"/><rect x="3" y="1" width="6" height="3" fill="#e6e6e6"/></svg>973.555.0187</li>
      <li><svg viewBox="0 0 12 12"><rect x="1" y="2.5" width="10" height="7" fill="#e6e6e6"/><path d="M1 2.5l5 4 5-4" stroke="#1c1d1f" fill="none"/></svg>reliefcare.office@mail.com</li>
      <li><svg viewBox="0 0 12 12"><circle cx="6" cy="6" r="5" fill="#e6e6e6"/><path d="M1 6h10M6 1v10" stroke="#1c1d1f" stroke-width=".8"/></svg>www.gentlereliefpc.com</li>
    </ul>
  </div>

  <div class="edge"></div>
</section>

<section class="card card--back" aria-label="Business card back">
  <h2 class="appt__title">Next Appointment</h2>
  <div class="field"><span>Name :</span><span class="field__line"></span></div>
  <div class="field"><span>Time :</span><span class="field__line"></span><span class="field__suffix">AM/PM</span></div>
  <div class="days">
    <span class="day">Mon <span class="day__box"></span></span>
    <span class="day">Tue <span class="day__box"></span></span>
    <span class="day">Wed <span class="day__box"></span></span>
    <span class="day">Thu <span class="day__box"></span></span>
    <span class="day">Fri <span class="day__box"></span></span>
    <span class="day">Sat <span class="day__box"></span></span>
  </div>
  <p class="note">Please give 24 hours notice if you are unable to keep your appointment or a cancellation fee may be charged.</p>
</section>

</body>
</html>
```